AV & Engineering company needs a Business Card Design

Like the simple design, don't too colorful. Smart & professional feel

Industry/Entity Type

Business

Requirements
Nice to have
• I would like to see the vertical design.

```html
<!DOCTYPE html>
<html lang="en">
<head>
<meta charset="utf-8">
<title>Norvale Systems Ltd – Business Card</title>
<link rel="stylesheet" href="https://fonts.googleapis.com/css2?family=Montserrat:wght@400;500;600;700&display=swap">
<style>
  :root {
    --bg: #e6e4e1;
    --paper: #f6f6f6;
    --red: #c8111a;
    --red-deep: #9c1219;
    --ink: #2f2f33;
    --ink-soft: #55565a;
  }
  * { margin: 0; padding: 0; box-sizing: border-box; }
  html, body {
    width: 1200px; height: 1091px; overflow: hidden;
    background: var(--bg);
    font-family: "Montserrat", Arial, sans-serif;
  }
  .sheet {
    width: 1200px; height: 1091px;
    display: flex; flex-direction: column; align-items: center; justify-content: center;
    gap: 60px;
  }
  .card {
    position: relative;
    width: 760px; height: 434px;
    background: var(--paper);
    box-shadow: 0 6px 18px rgba(0,0,0,0.18);
    overflow: hidden;
  }
  .accent-area {
    position: absolute;
    background: linear-gradient(135deg, var(--red), var(--red-deep));
  }
  .card-front .accent-area { left: 0; right: 0; bottom: 0; height: 120px; }
  .card-back .accent-area { top: 0; right: 0; bottom: 0; width: 150px; }
  .brand {
    position: absolute;
    display: flex; align-items: center; gap: 14px;
    color: var(--red);
    font-weight: 700;
    letter-spacing: 0.5px;
    white-space: nowrap;
  }
  .brand-mark { background: var(--red); display: block; }
  .card-front .brand { left: 110px; top: 118px; font-size: 34px; }
  .card-front .brand-mark { width: 40px; height: 40px; }
  .card-back .brand { left: 56px; top: 62px; font-size: 26px; }
  .card-back .brand-mark { width: 30px; height: 30px; }
  .holder {
    position: absolute; right: 190px; top: 128px; text-align: right;
  }
  .holder-name {
    color: var(--red); font-weight: 600; font-size: 27px; letter-spacing: 2px;
    white-space: nowrap;
  }
  .holder-role {
    color: var(--ink); font-weight: 500; font-size: 17px; margin-top: 2px;
  }
  .rule {
    position: absolute; left: 0; top: 204px; width: 420px; height: 2px; background: var(--red-deep);
  }
  .contact {
    position: absolute; left: 58px; top: 276px;
    list-style: none; color: var(--ink-soft); font-size: 19px; line-height: 34px;
  }
  .contact-label { display: inline-block; width: 36px; }
</style>
</head>
<body>
<main class="sheet">
  <section class="card card-front" aria-label="Card front">
    <div class="accent-area" role="img" aria-label="Decorative red accent area"></div>
    <div class="brand"><span class="brand-mark"></span>NORVALE SYSTEMS LTD</div>
  </section>

  <section class="card card-back" aria-label="Card back">
    <div class="accent-area" role="img" aria-label="Decorative red accent area"></div>
    <div class="brand"><span class="brand-mark"></span>NORVALE SYSTEMS LTD</div>
    <div class="holder">
      <p class="holder-name">DANIEL BROOKS</p>
      <p class="holder-role">Co-Founder &amp; CEO</p>
    </div>
    <div class="rule"></div>
    <ul class="contact">
      <li><span class="contact-label">T:</span>(415) 555-0182</li>
      <li><span class="contact-label">M:</span>daniel@norvalesystems.com</li>
      <li><span class="contact-label">W:</span>norvalesystems.com</li>
    </ul>
  </section>
</main>
</body>
</html>
```